Varlow Landscaping

Create a website for a new landscaping company. I have a logo already and description of services offered. I have a website that I would like all inquiries and appointments to get forwarded to. I need just need it well organized so that a husband and wife team can manage it easily. This is a company that will continue to grow over time and will need to add more services under new tabs over time. If you need the email where appointments and inquiries should go please send me a message.
Services offered are: Weekly/bi weekly mowing, weed eating and edging, Plant installation pinestraw & mulch installation, weed & feed, leaf removal and yard clean up.

```html
<!DOCTYPE html>
<html lang="en">
<head>
<meta charset="utf-8">
<title>Varlow Landscaping</title>
<link href="https://fonts.googleapis.com/css2?family=Poppins:ital,wght@0,400;0,500;0,600;0,700;1,400&display=swap" rel="stylesheet">
<style>
:root{
  --green:#11701f;
  --green-dark:#0b5a16;
  --green-soft:#eef5ee;
  --green-mist:#9fc4a2;
  --ink:#1d1d1d;
  --muted:#6b6b6b;
  --white:#ffffff;
  --footer:#2a2a2a;
  --star:#f2b01e;
}
*{box-sizing:border-box;margin:0;padding:0}
html,body{width:1200px;height:5001px;overflow:hidden}
body{position:relative;font-family:"Poppins",sans-serif;color:var(--ink);background:var(--white)}
.abs{position:absolute}
.btn{position:absolute;display:flex;align-items:center;justify-content:center;background:var(--green);color:var(--white);font-size:13px;font-weight:500}
.btn.light{background:var(--white);color:var(--green)}
.section-title{position:absolute;left:0;width:1200px;text-align:center;font-size:31px;font-weight:600}
.section-sub{position:absolute;left:0;width:1200px;text-align:center;font-size:13px;color:var(--muted);line-height:19px}
.photo{position:absolute}

/* hero */
.hero{left:0;top:0;width:1200px;height:705px;background:linear-gradient(180deg,#3d4a32 0%,#56683f 45%,#2f3d26 100%)}
.nav{left:136px;top:20px;width:928px;height:73px;background:var(--white);border-radius:40px;display:flex;align-items:center}
.brand{position:absolute;left:34px;top:0;height:73px;display:flex;align-items:center;gap:8px;font-size:11px;font-weight:600;line-height:13px;color:var(--green)}
.brand i{width:22px;height:22px;border-radius:50%;background:var(--green);display:block;flex:none}
.nav-links{position:absolute;left:186px;top:0;height:73px;display:flex;gap:32px;align-items:center;font-size:13px;color:#444}
.nav-links .active{color:var(--green);font-weight:500}
.hero-title{left:0;top:222px;width:1200px;text-align:center;color:var(--white);font-size:61px;font-weight:600;line-height:74px}
.hero-sub{left:230px;top:396px;width:740px;text-align:center;color:var(--white);font-size:13.5px;line-height:18px}

/* about */
.about-eyebrow{left:661px;top:878px;font-size:13px;color:var(--green)}
.about-title{left:661px;top:903px;font-size:30px;font-weight:600}
.about-text{left:661px;top:956px;width:370px;font-size:13px;line-height:19.6px;color:#555}
.badge{left:276px;top:960px;width:208px;height:208px;border-radius:50%;background:var(--white);display:flex;align-items:center;justify-content:center;text-align:center;font-size:19px;font-weight:600;color:var(--green);line-height:24px}

/* services */
.svc-head{left:161px;top:1535px;font-size:30px;font-weight:600}
.svc-sub{left:161px;top:1583px;width:250px;font-size:13px;line-height:17px;color:var(--muted)}
.card{position:absolute;width:254px;height:334px;background:var(--green-soft)}
.card.white{background:var(--white)}
.card .pic{position:absolute;left:0;top:0;width:254px;height:180px}
.card .ico{position:absolute;right:14px;top:146px;width:64px;height:64px;border-radius:50%;background:var(--green-soft);border:4px solid var(--white);display:flex;align-items:center;justify-content:center}
.card h3{position:absolute;left:12px;top:206px;width:170px;font-size:14px;font-weight:600;line-height:18px}
.card p{position:absolute;left:12px;top:250px;width:200px;font-size:12px;line-height:14px;color:#666}
.card .more{position:absolute;left:12px;top:300px;display:flex;align-items:center;gap:8px;font-size:11px;font-weight:500;color:#333}
.card .more i{width:16px;height:16px;border-radius:50%;background:var(--green);display:block;position:relative}
.card .more i::after{content:"";position:absolute;left:4px;top:5px;width:5px;height:5px;border-top:1.5px solid #fff;border-right:1.5px solid #fff;transform:rotate(45deg)}

/* why */
.step-title{position:absolute;width:240px;text-align:center;font-size:15.5px;font-weight:600;line-height:24px}
.step-text{position:absolute;width:200px;text-align:center;font-size:11.5px;line-height:22px;color:#888}
.step-circle{position:absolute;border-radius:50%;display:flex;align-items:center;justify-content:center}
.step-num{position:absolute;width:40px;height:40px;border-radius:50%;background:var(--green);color:#fff;font-style:italic;font-size:14px;display:flex;align-items:center;justify-content:center;font-family:Georgia,serif}

/* projects */
.proj-card{left:443px;top:3288px;width:312px;height:107px;background:var(--white);text-align:center}
.proj-card h4{margin-top:22px;font-size:16px;font-weight:600}
.proj-card p{font-size:12.5px;line-height:16px;color:#555;margin-top:8px}

/* testimonials */
.quote{position:absolute;width:404px}
.quote .stars{font-size:15px;color:var(--star);letter-spacing:1px}
.quote .stars b{color:var(--ink);font-size:12.5px;font-weight:500;margin-left:6px}
.quote p{margin-top:6px;font-size:12.5px;font-style:italic;line-height:19.5px;color:#555}
.quote .who{position:absolute;left:0;top:160px;display:flex;align-items:center;gap:18px}
.avatar{width:52px;height:52px;border-radius:50%;background:linear-gradient(160deg,#c9c3bd,#7d746d)}
.who .name{font-size:14px;color:#444;line-height:20px}
.who .org{font-size:14px;font-weight:600}
.qmark{position:absolute;right:0;top:162px;font-size:80px;line-height:80px;color:var(--green-mist);font-family:Georgia,serif;font-weight:700}

/* contact */
.contact-card{left:348px;top:4132px;width:503px;height:578px;background:var(--white);box-shadow:0 6px 30px rgba(0,0,0,.08)}
.field{position:absolute;border-bottom:1px solid #ccc;font-size:11px;color:#888;padding-bottom:14px}
.robot{position:absolute;left:139px;top:422px;width:226px;height:54px;border:1px solid #ddd;background:#f9f9f9;border-radius:3px;display:flex;align-items:center;gap:12px;padding-left:12px;font-size:11px;color:#444}
.robot i{width:20px;height:20px;border:2px solid #bbb;background:#fff;display:block}
.robot s{position:absolute;right:14px;top:14px;width:26px;height:26px;background:#c9d6ea;display:block}

/* footer */
.footer{left:0;top:4710px;width:1200px;height:291px;background:var(--footer);color:#fff}
.f-brand{position:absolute;left:150px;top:84px;width:220px;text-align:center;font-size:18px;font-weight:600;line-height:26px;white-space:nowrap;color:var(--green-mist)}
.f-brand i{display:block;width:72px;height:72px;margin:0 auto 10px;border-radius:50%;border:5px solid var(--green-mist)}
.socials{position:absolute;left:202px;top:220px;display:flex;gap:26px}
.socials i{width:16px;height:16px;border-radius:50%;border:2px solid #fff;display:block}
.f-col{position:absolute;top:70px;font-size:13px;line-height:38px}
.f-col h5{font-size:16px;font-weight:600;line-height:24px;margin-bottom:16px}
.f-contact li{list-style:none;display:flex;align-items:center;gap:14px;height:38px}
.f-contact i{width:22px;height:22px;border-radius:50%;background:var(--green);display:flex;align-items:center;justify-content:center}
</style>
</head>
<body>

<!-- HERO -->
<section class="abs hero" role="img" aria-label="Gardener trimming a lawn with a string trimmer among trees"></section>
<svg class="abs" style="left:0;top:640px" width="1200" height="70" viewBox="0 0 1200 70" preserveAspectRatio="none"><path d="M0 30 Q150 5 300 28 T600 22 T900 30 T1200 18 V70 H0Z" fill="#fff"/></svg>
<nav class="abs nav">
  <div class="brand"><i></i><span>Varlow<br>Landscaping</span></div>
  <div class="nav-links"><span class="active">Home</span><span>About Us</span><span>Services</span><span>Projects</span><span>Testimonial</span><span>Contact Us</span></div>
  <div class="btn" style="left:757px;top:17px;width:146px;height:41px;font-size:13px">Get In Touch</div>
</nav>
<h1 class="abs hero-title">Reliable Lawn Care &amp;<br>Landscaping Services</h1>
<p class="abs hero-sub">Elevate your environment with our unrivaled expertise and passion for excellence! Our rich legacy to your green dreams into reality.</p>
<div class="btn light" style="left:532px;top:452px;width:136px;height:38px">Learn More</div>

<!-- ABOUT -->
<div class="photo" style="left:160px;top:812px;width:215px;height:518px;background:linear-gradient(160deg,#c3a05a,#4f8a32 55%,#2e6a22)" role="img" aria-label="Worker planting seedlings"></div>
<div class="photo" style="left:385px;top:812px;width:213px;height:518px;background:linear-gradient(170deg,#566d3a,#7b9a4c 60%,#b0a168)" role="img" aria-label="Man trimming lawn edges"></div>
<div class="abs badge">Varlow<br>Landscaping</div>
<div class="abs about-eyebrow">About Us</div>
<h2 class="abs about-title">We Provide Best Services</h2>
<p class="abs about-text">Lorem Ipsum is simply dummy text of the printing and typesetting industry. Lorem Ipsum has been the industry's standard dummy text ever since the 1500s, when an unknown printer took a galley of type and scrambled it to make a type specimen book. It has survived not only five centuries, but also the leap into electronic typesetting, remaining essentially unchanged. Lorem Ipsum is simply dummy text of the printing and typesetting industry. Lorem Ipsum has been the industry's standard dummy text ever since the 1500s, when an unknown printer took a galley of type and scrambled it to make a unchanged.</p>
<div class="btn" style="left:661px;top:1222px;width:138px;height:37px">Learn More</div>

<!-- SERVICES -->
<svg class="abs" style="left:0;top:1915px" width="1200" height="300" viewBox="0 0 1200 300" preserveAspectRatio="none"><path d="M0 40 Q300 -10 600 30 T1200 20 V300 H0Z" fill="var(--green)"/></svg>
<h2 class="abs svc-head">Our Services</h2>
<p class="abs svc-sub">Discover tailored garden and landscape solutions.</p>
<div class="btn" style="left:161px;top:1639px;width:146px;height:38px">View All Services</div>

<div class="card" style="left:472px;top:1447px">
  <div class="pic" style="background:linear-gradient(160deg,#6da443,#c0392b 50%,#4e8a30)" role="img" aria-label="Red lawn mower on grass"></div>
  <div class="ico"><svg width="30" height="30" viewBox="0 0 30 30" fill="none" stroke="var(--green)" stroke-width="2"><circle cx="9" cy="22" r="4"/><circle cx="22" cy="22" r="4"/><path d="M5 18h20l-3-8H10zM22 10l4-7"/></svg></div>
  <h3>Weekly/Bi Weekly Mowing</h3><p>Investment Planning Working with around at laboret.</p><div class="more">LEARN MORE<i></i></div>
</div>
<div class="card" style="left:773px;top:1447px">
  <div class="pic" style="background:linear-gradient(160deg,#4d5a2e,#6b5a3c 55%,#3e5a24)" role="img" aria-label="Hand digging weeds from soil"></div>
  <div class="ico"><svg width="30" height="30" viewBox="0 0 30 30" fill="none" stroke="var(--green)" stroke-width="2"><path d="M6 24l10-10M14 8l8 8M18 4l8 8-4 4-8-8z"/></svg></div>
  <h3>Weed Eating and Edging</h3><p>Investment Planning Working with around at laboret.</p><div class="more">LEARN MORE<i></i></div>
</div>
<div class="card white" style="left:173px;top:1816px">
  <div class="pic" style="background:linear-gradient(160deg,#3e5e2a,#5c4632 55%,#2f4a20)" role="img" aria-label="Seedlings in trays"></div>
  <div class="ico"><svg width="30" height="30" viewBox="0 0 30 30" fill="none" stroke="var(--green)" stroke-width="2"><path d="M15 26V12M15 12c-6 0-8-6-8-8 6 0 8 4 8 8zM15 16c5 0 8-4 8-8-5 0-8 4-8 8M5 20h20"/></svg></div>
  <h3>Plant Installation Pinestraw</h3><p>Investment Planning Working with around at laboret.</p><div class="more">LEARN MORE<i></i></div>
</div>
<div class="card white" style="left:472px;top:1816px">
  <div class="pic" style="background:linear-gradient(160deg,#54793a,#8fae6c 55%,#3c6226)" role="img" aria-label="Gloved hands holding a plant"></div>
  <div class="ico"><svg width="30" height="30" viewBox="0 0 30 30" fill="none" stroke="var(--green)" stroke-width="2"><path d="M5 26h20M9 26V14M15 26V8M21 26V14M9 14l-3-4M15 8l3-4M21 14l3-4"/></svg></div>
  <h3>Weed &amp; Feed</h3><p>Investment Planning Working Investment Planning Working with around at laboret.</p><div class="more">LEARN MORE<i></i></div>
</div>
<div class="card white" style="left:762px;top:1816px;width:276px">
  <div class="pic" style="width:254px;left:11px;background:linear-gradient(160deg,#8ca04a,#b07a3a 55%,#4a7ac0)" role="img" aria-label="Blue rake gathering autumn leaves"></div>
  <div class="ico" style="right:25px"><svg width="30" height="30" viewBox="0 0 30 30" fill="none" stroke="var(--green)" stroke-width="2"><path d="M8 26L22 6M18 4l8 6M4 24l6 2"/></svg></div>
  <h3 style="left:23px">Leaf Removal and Yard Clean Up</h3><p style="left:23px">Investment Planning Working with around at laboret.</p><div class="more" style="left:23px">LEARN MORE<i></i></div>
</div>

<!-- WHY -->
<h2 class="section-title" style="top:2300px">Why We Are The Best Company</h2>
<p class="section-sub" style="top:2356px">Discover tailored garden and landscape solutions. and mect vaiues,<br>vemioreal tihrough tionrgs or venuersiond abilites.</p>
<svg class="abs" style="left:0;top:2500px" width="1200" height="140" viewBox="0 0 1200 140" fill="none" stroke="var(--green)" stroke-width="1.5" stroke-dasharray="5 5"><path d="M175 128 L232 110"/><path d="M330 70 L490 18"/><path d="M655 38 L860 110"/><path d="M965 110 L1020 128"/><path d="M1012 122l8 6-9 2" stroke-dasharray="none"/></svg>
<div class="step-circle" style="left:224px;top:2533px;width:100px;height:100px;background:var(--green-soft);border:2px dashed var(--green-mist)"><svg width="36" height="36" viewBox="0 0 36 36" fill="none" stroke="var(--green)" stroke-width="2"><path d="M10 30V14M8 8h4v6H8zM24 30V16M20 8c0 4 8 4 8 0v8h-8z"/></svg></div>
<div class="step-num" style="left:295px;top:2527px">01</div>
<div class="step-circle" style="left:538px;top:2449px;width:116px;height:116px;background:var(--green)"><svg width="40" height="40" viewBox="0 0 36 36" fill="none" stroke="#fff" stroke-width="2"><path d="M12 30V18M24 30V18M10 18h16M18 6v12M14 10l4-4 4 4"/></svg></div>
<div class="step-num" style="left:618px;top:2452px;background:#fff;color:var(--green)">02</div>
<div class="step-circle" style="left:868px;top:2533px;width:100px;height:100px;background:var(--green-soft);border:2px dashed var(--green-mist)"><svg width="36" height="36" viewBox="0 0 36 36" fill="none" stroke="var(--green)" stroke-width="2"><path d="M8 28L28 8M8 8l20 20"/><circle cx="10" cy="26" r="3"/></svg></div>
<div class="step-num" style="left:938px;top:2527px">03</div>
<div class="step-title" style="left:155px;top:2664px">Grass Care Garden<br>Services</div>
<div class="step-text" style="left:175px;top:2720px">Ensuring optimal water levels is essential level.</div>
<div class="abs" style="left:484px;top:2608px;width:227px;height:146px;background:#fff;box-shadow:0 6px 24px rgba(0,0,0,.08)"></div>
<svg class="abs" style="left:586px;top:2594px" width="24" height="16"><path d="M0 16L12 2 24 16Z" fill="#fff"/></svg>
<div class="step-title" style="left:478px;top:2634px">Seasonal tidying and<br>maintenance</div>
<div class="step-text" style="left:497px;top:2689px">Ensuring optimal water levels is essential level.</div>
<div class="step-title" style="left:799px;top:2664px">Tailored landscaping<br>Solutions</div>
<div class="step-text" style="left:819px;top:2720px">Ensuring optimal water levels is essential level.</div>
<svg class="abs" style="left:412px;top:2658px" width="30" height="20" fill="none" stroke="#888" stroke-width="1.5"><path d="M4 3l8 7-8 7M14 3l8 7-8 7"/></svg>
<svg class="abs" style="left:756px;top:2658px" width="30" height="20" fill="none" stroke="#888" stroke-width="1.5"><path d="M4 3l8 7-8 7M14 3l8 7-8 7"/></svg>

<!-- PROJECTS -->
<h2 class="section-title" style="top:2837px">Our Projects</h2>
<p class="section-sub" style="top:2896px">Discover tailored garden and landscape solutions. and mect vaiues,<br>vemioreal tihrough tionrgs or venuersiond abilites.</p>
<svg class="abs" style="left:0;top:3140px" width="1200" height="440" viewBox="0 0 1200 440" preserveAspectRatio="none"><path d="M0 20 Q300 0 600 10 T1200 15 V380 Q900 330 600 380 T0 420Z" fill="var(--green)"/><path d="M0 420 Q300 360 600 380 T1200 380 V440 H0Z" fill="var(--green-mist)"/></svg>
<div class="photo" style="left:107px;top:2985px;width:314px;height:410px;background:linear-gradient(170deg,#7a9a5c,#5f7e44 50%,#d2552a 85%)" role="img" aria-label="Man with lawn mower beside a gazebo"></div>
<div class="photo" style="left:443px;top:2985px;width:312px;height:303px;background:linear-gradient(160deg,#4e7434,#7b6148 50%,#36602a)" role="img" aria-label="Gardener tending shrubs"></div>
<div class="abs proj-card"><h4>Garden Maintenance</h4><p>Varlow Enterprise gives comsiders<br>or venuersiond abilites.</p></div>
<div class="photo" style="left:777px;top:2985px;width:314px;height:410px;background:linear-gradient(160deg,#cfd8c4,#3fa7b8 45%,#2f6a24)" role="img" aria-label="Two gardeners working with potted plants"></div>
<svg class="abs" style="left:575px;top:3428px" width="50" height="18"><circle cx="8" cy="9" r="3" fill="#fff"/><circle cx="25" cy="9" r="6" fill="none" stroke="#fff" stroke-width="1.5"/><circle cx="25" cy="9" r="3" fill="#fff"/><circle cx="42" cy="9" r="3" fill="#fff"/></svg>
<div class="btn light" style="left:522px;top:3476px;width:154px;height:37px">View All Projects</div>

<!-- TESTIMONIALS -->
<svg class="abs" style="left:0;top:3560px" width="1200" height="30" viewBox="0 0 1200 30" preserveAspectRatio="none"><path d="M0 0 H1200 V5 Q600 40 0 10Z" fill="#fff"/></svg>
<h2 class="section-title" style="top:3624px">Our Testimonial</h2>
<p class="section-sub" style="top:3683px">Discover tailored garden and landscape solutions. and mect vaiues,<br>vemioreal tihrough tionrgs or venuersiond abilites.</p>
<div class="quote" style="left:161px;top:3766px;height:240px">
  <div class="stars">★★★★★<b>5.0</b></div>
  <p>There are many variations of passages of Lorem Ipsum available, but the majority have suffered alteration in some form, by injected humour, you need to be sure there isn't anything embarrassing hidden in the middle of text. All the tend to repeat predefined chunks as necess.</p>
  <div class="who"><div class="avatar" role="img" aria-label="Client portrait"></div><div><div class="name">Mara Ellison</div><div class="org">Fernwick Holdings Ltd.</div></div></div>
  <div class="qmark">&ldquo;</div>
</div>
<div class="quote" style="left:635px;top:3766px;height:240px">
  <div class="stars">★★★★★<b>5.0</b></div>
  <p>There are many variations of passages of Lorem Ipsum available, but the majority have suffered alteration in some form, by injected humour, you need to be sure there isn't anything embarrassing hidden in the middle of text. All the tend to repeat predefined chunks as necess.</p>
  <div class="who"><div class="avatar" role="img" aria-label="Client portrait"></div><div><div class="name">Mara Ellison</div><div class="org">Fernwick Holdings Ltd.</div></div></div>
  <div class="qmark">&ldquo;</div>
</div>
<div class="btn" style="left:511px;top:4020px;width:178px;height:38px">View All Testimonial</div>

<!-- CONTACT -->
<svg class="abs" style="left:0;top:4330px" width="1200" height="380" viewBox="0 0 1200 380" preserveAspectRatio="none" role="img" aria-label="Lawn mower on fresh green grass"><defs><linearGradient id="lawn" x1="0" y1="0" x2="1" y2="0"><stop offset="0" stop-color="#5f8f36"/><stop offset=".2" stop-color="#b33a26"/><stop offset=".35" stop-color="#6e9b3c"/><stop offset="1" stop-color="#4f8a2c"/></linearGradient></defs><path d="M0 250 Q300 -20 600 0 T1200 250 V380 H0Z" fill="url(#lawn)"/></svg>
<div class="abs contact-card">
  <div class="abs" style="left:0;top:57px;width:503px;text-align:center;font-size:12px;color:#555">Contact</div>
  <h2 class="abs" style="left:0;top:76px;width:503px;text-align:center;font-size:29px;font-weight:600">Get In Touch</h2>
  <div class="field" style="left:58px;top:150px;width:176px">Name*</div>
  <div class="field" style="left:275px;top:150px;width:176px">Last Name</div>
  <div class="field" style="left:58px;top:212px;width:176px">Phone</div>
  <div class="field" style="left:275px;top:212px;width:176px">Email Address*</div>
  <div class="field" style="left:58px;top:274px;width:393px">Service</div>
  <div class="field" style="left:58px;top:336px;width:393px;height:78px">Your Message</div>
  <div class="robot"><i></i>I'm not a robot<s></s></div>
  <div class="btn" style="left:176px;top:498px;width:152px;height:37px">SUBMIT</div>
</div>

<!-- FOOTER -->
<footer class="abs footer">
  <div class="f-brand"><i></i>Varlow Landscaping</div>
  <div class="socials"><i></i><i></i><i></i></div>
  <div class="f-col" style="left:437px"><h5>Quick Links</h5>Home<br>About Us<br>Services<br>Contact Us</div>
  <div class="f-col" style="left:612px"><h5>Services</h5>Weekly/Bi Weekly Mowing<br>Weed Eating and Edging<br>Plant Installation Pinestraw<br>Weed &amp; Feed</div>
  <div class="f-col f-contact" style="left:847px"><h5>Contact Us</h5>
    <ul>
      <li><i><svg width="12" height="12" viewBox="0 0 12 12" fill="#fff"><path d="M2 1l2 0 1 3-1.5 1a6 6 0 003 3L8 7l3 1v2c0 .6-.4 1-1 1A9 9 0 011 2c0-.6.4-1 1-1z"/></svg></i>555-010-4821</li>
      <li><i><svg width="12" height="10" viewBox="0 0 12 10" fill="none" stroke="#fff" stroke-width="1.4"><rect x="1" y="1" width="10" height="8"/><path d="M1 1l5 4 5-4"/></svg></i>hello@varlowlandscaping.com</li>
      <li><i><svg width="10" height="13" viewBox="0 0 10 13" fill="#fff"><path d="M5 0a5 5 0 015 5c0 3-5 8-5 8S0 8 0 5a5 5 0 015-5zm0 3a2 2 0 100 4 2 2 0 000-4z"/></svg></i>122, Lorem ipsum dolird</li>
    </ul>
  </div>
</footer>

</body>
</html>
```